Tampa Bay fishing guide needs stunning website.

I currently have a site - www.reelcoastcharters.example which I personally put together using the Plimo platform and I am looking for a redesign on a different platform (Sitebarn?) that will allow me to easily create landing pages in the future. Would like to have a block for visitors to opt in to newsletter. Need social media links on all pages.

I would like to let my visitors know that I am able to handle their fishing charter needs here in the Tampa Bay area, if I'm not available for the dates they are looking to go I can refer them to a reputable captain in the area.

Target Market(s)

United States

Industry/Entity Type

Tourism

Coding

Coded - Design and coding required

Number of Pages Required

5+ page

Font styles to use
Sans Serif

Colors
0355a3
3176b5
85abd2
fbf289

Requirements
Must have
• Mobile Responsive, Ability to insert Trackwise Metrics, Chatterly pixels, ability to add custom landing pages in future
Nice to have
• Clean, easy navigation

```html
<!DOCTYPE html>
<html lang="en">
<head>
<meta charset="utf-8">
<title>Capt. Wade Harlan – Tampa Bay Fishing Charters</title>
<link rel="stylesheet" href="https://fonts.googleapis.com/css2?family=Raleway:wght@600;700;800&family=Open+Sans:ital,wght@0,400;0,600;0,700;1,600&display=swap">
<style>
:root{
  --blue-deep:#0355a3;
  --blue:#3176b5;
  --blue-light:#85abd2;
  --yellow:#fbf289;
  --heading:#14509a;
  --ink:#2b2b2b;
  --muted:#666;
  --card-bg:#ececec;
  --footer:#0b55a2;
  --white:#fff;
}
*{box-sizing:border-box;margin:0;padding:0}
html,body{width:1200px;height:2808px;overflow:hidden}
body{font-family:"Open Sans",Arial,sans-serif;color:var(--ink);background:var(--white);position:relative}
.wrap{width:878px;margin:0 auto;position:relative}
h1,h2,h3,h4{font-family:"Raleway",Arial,sans-serif}

/* header */
.site-header{height:97px;border-top:4px solid var(--blue-deep);position:relative}
.brand{position:absolute;left:161px;top:26px;display:flex;align-items:center;gap:10px;color:var(--blue-deep);font:700 26px "Raleway",sans-serif}
.brand-dot{width:14px;height:14px;border-radius:50%;background:var(--blue-light)}
.call{position:absolute;right:161px;top:22px;font-size:13px;color:#333;letter-spacing:.3px}
.call b{color:var(--blue-deep)}
.main-nav{position:absolute;right:161px;top:62px;display:flex;gap:35px;font-size:11.5px;font-weight:600;color:#333}
.main-nav .active{color:var(--blue-deep)}

/* hero */
.hero{position:relative;height:573px;overflow:hidden;background:
  radial-gradient(ellipse 260px 170px at 560px 420px,rgba(210,225,220,.55),transparent 70%),
  radial-gradient(ellipse 300px 330px at 880px 260px,rgba(235,232,225,.75),transparent 70%),
  radial-gradient(ellipse 180px 260px at 1120px 180px,rgba(245,245,242,.9),transparent 70%),
  radial-gradient(ellipse 200px 150px at 980px 520px,rgba(120,150,175,.6),transparent 70%),
  linear-gradient(100deg,#0f3a2c 0%,#17503e 38%,#2d6a56 58%,#7f9a90 78%,#cfd4d1 100%)}
.hero-copy{position:absolute;left:161px;top:280px;color:var(--white);width:440px}
.hero-copy h1{font-size:26px;line-height:42px;font-weight:700;letter-spacing:.3px}
.hero-copy p{font-size:15px;font-weight:600;line-height:24px;margin-top:10px}
.btn{display:inline-block;background:var(--yellow);color:#333;font:700 11px "Open Sans",sans-serif;padding:9px 17px;text-transform:uppercase}
.hero-copy .btn{margin-top:18px}
.play{position:absolute;left:869px;top:336px;width:96px;height:96px}
.dots{position:absolute;left:562px;top:526px;display:flex;gap:5px}
.dots span{width:12px;height:12px;border-radius:50%;background:var(--white)}
.dots .on{background:var(--yellow)}

/* intro */
.intro{padding-top:42px;height:493px;text-align:center}
.section-title{font-size:24px;font-weight:700;color:var(--heading);letter-spacing:.4px}
.intro p{font-size:11px;line-height:19px;color:var(--muted);margin:16px auto 0;width:860px}
.cards{display:flex;gap:11px;margin-top:24px;text-align:left}
.card{width:211px;background:var(--card-bg);position:relative;height:274px}
.card .photo{height:189px}
.card h4{font:600 13px/20px "Open Sans",sans-serif;color:#333;padding:12px 30px 0 18px}
.arrow{position:absolute;right:0;bottom:0;width:22px;height:20px;background:var(--blue-deep);display:flex;align-items:center;justify-content:center}

/* feature bands */
.band{display:flex;height:329px}
.band .pane{width:600px;height:329px;position:relative}
.band-copy{color:var(--white)}
.band-copy h2{position:absolute;top:60px;font-size:22px;color:var(--yellow);font-weight:700}
.band-copy h3{position:absolute;top:104px;font:600 17px "Open Sans",sans-serif}
.band-copy p{position:absolute;top:138px;width:410px;font-size:10.5px;line-height:18px;opacity:.92}
.band-copy .btn{position:absolute;top:246px}
.charters .band-copy{background:var(--blue)}
.charters .band-copy>*{left:161px}
.pickup .band-copy{background:var(--blue-deep)}
.pickup .band-copy>*{left:36px}

/* destinations */
.destinations{height:463px;padding-top:46px;text-align:center}
.destinations .section-title{color:#111;font-size:22px}
.destinations p{font-size:11px;line-height:17px;color:var(--muted);width:760px;margin:12px auto 0}
.destinations .cards{gap:23px;margin-top:22px}
.destinations .card{width:277px;height:275px}
.destinations .card .photo{height:190px}

/* newsletter */
.newsletter{height:183px;position:relative;background:
  radial-gradient(ellipse 300px 160px at 620px 120px,rgba(70,90,100,.45),transparent 70%),
  radial-gradient(ellipse 200px 120px at 300px 60px,rgba(60,75,80,.35),transparent 70%),
  linear-gradient(180deg,#0a0f12,#1a2529 55%,#0a0f11);text-align:center;color:var(--white)}
.newsletter h2{padding-top:26px;font-size:22px;font-weight:700;letter-spacing:.4px}
.newsletter .tag{font-style:italic;font-weight:600;font-size:14px;margin-top:4px}
.signup{position:absolute;left:331px;top:97px;width:537px;height:49px;background:#9a9a9a;padding:5px;display:flex}
.signup .field{flex:1;background:var(--white);color:#777;font-size:12px;text-align:left;padding:11px 14px}
.signup .submit{width:90px;background:var(--blue-deep);font:700 11px "Open Sans",sans-serif;display:flex;align-items:center;justify-content:center}

/* footer */
.site-footer{height:337px;background:var(--footer);color:var(--white);position:relative}
.footer-brand{position:absolute;left:161px;top:42px;display:flex;align-items:center;gap:8px;font:700 22px "Raleway",sans-serif}
.footer-brand .brand-dot{width:12px;height:12px;background:var(--white)}
.footer-about{position:absolute;left:161px;top:118px;width:210px;font-size:10.5px;line-height:18px}
.payments{position:absolute;left:161px;top:200px;display:flex;gap:5px}
.payments span{width:32px;height:20px;background:var(--white);border-radius:2px}
.footer-col{position:absolute;top:58px}
.footer-col h4{font:700 16px "Raleway",sans-serif;color:var(--yellow);margin-bottom:12px}
.footer-col li{list-style:none;font-size:11px;line-height:23px}
.col-services{left:425px}
.col-contact{left:573px}
.col-contact li{display:flex;align-items:center;gap:8px}
.col-contact li.sub{padding-left:16px}
.col-badges{left:803px}
.badges{display:flex;gap:6px}
.badges .badge{width:114px;height:93px;background:var(--white);border-top:14px solid #6aa842}
.badges .badge.b2{width:108px;border-top-color:#1a6fb8}
.footer-bar{position:absolute;left:161px;right:161px;top:258px;border-top:1px solid rgba(255,255,255,.25);display:flex;justify-content:space-between;align-items:center;padding-top:24px;font-size:10px}
.social{display:flex;gap:10px}
.social span{width:26px;height:26px;border-radius:50%;border:1.5px solid var(--white)}
</style>
</head>
<body>

<header class="site-header">
  <div class="brand"><span class="brand-dot"></span>Capt. Wade Harlan</div>
  <div class="call">CALL CAPT. WADE <b>(555) 014-2290</b></div>
  <nav class="main-nav">
    <span class="active">HOME</span><span>ABOUT US</span><span>PICK UP LOCATIONS</span><span>RATES</span><span>CONTACT US</span><span>GIFT CARD</span>
  </nav>
</header>

<section class="hero" role="img" aria-label="Anglers on a boat landing a large tarpon from green bay water">
  <div class="hero-copy">
    <h1>TAMPA BAY, FISHING GUIDE<br>TAMPA BAY FISHING CHARTERS</h1>
    <p>Sed ut perspiciatis unde omnis iste natus error sit voluptatem accusa ntium doloremque laudantium, totam rem aper</p>
    <span class="btn">Read More</span>
  </div>
  <svg class="play" viewBox="0 0 96 96" aria-hidden="true"><circle cx="48" cy="48" r="44" fill="rgba(0,0,0,.35)" stroke="#fff" stroke-width="5"/><path d="M38 30 L66 48 L38 66Z" fill="#fff"/></svg>
  <div class="dots"><span></span><span class="on"></span><span></span><span></span><span></span></div>
</section>

<section class="intro">
  <div class="wrap">
    <h2 class="section-title">TAMPA BAY, FISHING GUIDE, TAMPA BAY FISHING CHARTERS</h2>
    <p>Capt. Wade Harlan, with over 20 years' experience. Native fishing charter tampa charter captain offering full and half day fishing charters on the waters of Tampa Bay. If you're looking for a great fishing charter tampa don't hesitate to contact Capt. Wade or you can simply book your trip online here. Come enjoy a wonderful day fishing charters Tampa for Tarpon, Snook, Redfish, Trout, Sharks, Cobia, Spanish mackerel as well as others aboard Capt. Wade Harlan Sport Fishing Charters boat.</p>
    <div class="cards">
      <div class="card"><div class="photo" role="img" aria-label="Angler fighting a fish at night from the boat" style="background:radial-gradient(ellipse 90px 60px at 80px 130px,rgba(150,180,200,.6),transparent 70%),radial-gradient(ellipse 130px 40px at 110px 175px,rgba(230,235,238,.85),transparent 70%),linear-gradient(180deg,#06140d,#0f2a1e 55%,#3d5a66)"></div><h4>Sed ut perspiciatisun de omnis iste nloreatrsit volu lore ptatem</h4><span class="arrow"><svg width="8" height="10" viewBox="0 0 8 10"><path d="M2 1l4 4-4 4" stroke="#fff" stroke-width="1.6" fill="none"/></svg></span></div>
      <div class="card"><div class="photo" role="img" aria-label="Two anglers holding a tarpon beside the boat" style="background:radial-gradient(ellipse 70px 80px at 60px 90px,rgba(240,240,238,.9),transparent 70%),radial-gradient(ellipse 60px 90px at 150px 130px,rgba(200,205,200,.7),transparent 70%),linear-gradient(160deg,#2f4a44,#52706a 50%,#1f3a34)"></div><h4>Sed ut perspiciatisun de omnis iste nloreatrsit volu lore ptatem</h4><span class="arrow"><svg width="8" height="10" viewBox="0 0 8 10"><path d="M2 1l4 4-4 4" stroke="#fff" stroke-width="1.6" fill="none"/></svg></span></div>
      <div class="card"><div class="photo" role="img" aria-label="Angler reeling in with a bent rod" style="background:radial-gradient(ellipse 60px 80px at 70px 110px,rgba(250,250,248,.9),transparent 70%),radial-gradient(ellipse 90px 50px at 140px 170px,rgba(60,60,58,.7),transparent 70%),linear-gradient(170deg,#dcdcd6,#b4b4ac 55%,#5c5c55)"></div><h4>Sed ut perspiciatisun de omnis iste nloreatrsit volu lore ptatem</h4><span class="arrow"><svg width="8" height="10" viewBox="0 0 8 10"><path d="M2 1l4 4-4 4" stroke="#fff" stroke-width="1.6" fill="none"/></svg></span></div>
      <div class="card"><div class="photo" role="img" aria-label="Guest holding a spotted sea trout on the water" style="background:radial-gradient(ellipse 60px 90px at 110px 130px,rgba(40,35,35,.55),transparent 70%),radial-gradient(ellipse 110px 30px at 110px 120px,rgba(220,215,200,.8),transparent 70%),linear-gradient(180deg,#7eaed6,#a9c8e0 45%,#4f7890 60%,#6d8fa3)"></div><h4>Sed ut perspiciatisun de omnis iste nloreatrsit volu lore ptatem</h4><span class="arrow"><svg width="8" height="10" viewBox="0 0 8 10"><path d="M2 1l4 4-4 4" stroke="#fff" stroke-width="1.6" fill="none"/></svg></span></div>
    </div>
  </div>
</section>

<section class="band charters">
  <div class="pane band-copy">
    <h2>FULL &amp; HALF DAY CHARTERS</h2>
    <h3>Sed ut perspiciatis unde omnis iste natusit volup</h3>
    <p>Sed ut perspiciatis unde omnis iste natus error sit voluptatem accusantium dolore mque laudantium, totam rem aperiam, eaque ipsa quae ab illo inventore veritatis et quasi architecto beatae vitae dicta sunt explicabomo enim ipsam volut ut perspiciatis unde omnis iste natus error sit voluptatem accusantium dolore mque laudantium, totam rem aperiam, eaque ipsa quae ab illo.</p>
    <span class="btn">Read More</span>
  </div>
  <div class="pane" role="img" aria-label="Anglers at the rail as a tarpon leaps and splashes beside the boat" style="background:radial-gradient(ellipse 200px 90px at 400px 150px,rgba(225,232,228,.85),transparent 70%),radial-gradient(ellipse 120px 140px at 130px 220px,rgba(215,205,185,.8),transparent 70%),radial-gradient(ellipse 300px 60px at 400px 290px,rgba(245,245,245,.9),transparent 70%),linear-gradient(180deg,#0f3326,#1f4d3c 60%,#cfd6d3)"></div>
</section>

<section class="band pickup">
  <div class="pane" role="img" aria-label="Captain in a blue shirt holding a large snook with mangroves behind" style="background:radial-gradient(ellipse 170px 170px at 190px 220px,rgba(30,90,190,.95),transparent 70%),radial-gradient(ellipse 280px 50px at 300px 230px,rgba(200,195,170,.8),transparent 70%),linear-gradient(180deg,#2c4a2a,#46673f 32%,#7d95a0 55%,#a9b7bd)"></div>
  <div class="pane band-copy">
    <h2>MULTIPLE PICKUP POINTS</h2>
    <h3>Sed ut perspiciatis unde omnis iste natusit volup</h3>
    <p>Sed ut perspiciatis unde omnis iste natus error sit voluptatem accusantium dolore mque laudantium, totam rem aperiam, eaque ipsa quae ab illo inventore veritatis et quasi architecto beatae vitae dicta sunt explicabomo enim ipsam volut ut perspiciatis unde omnis iste natus error sit voluptatem accusantium dolore mque laudantium, totam rem aperiam, eaque ipsa quae ab illo.</p>
    <span class="btn">Read More</span>
  </div>
</section>

<section class="destinations">
  <div class="wrap">
    <h2 class="section-title">OUR DESTINATIONS</h2>
    <p>Sed ut perspiciatis unde omnis iste natus error sit voluptatem accusantium doloremque laudantium, totam rem aperiam, eaque ipsa quae ab illo inventore veritatis et quasi architecto beatae vitae dicta sunt explicabo. Nemo enim ipsam voluptatem quia volup.</p>
    <div class="cards">
      <div class="card"><div class="photo" role="img" aria-label="Two anglers showing a snook on the bay" style="background:radial-gradient(ellipse 110px 90px at 140px 120px,rgba(60,140,190,.7),transparent 70%),radial-gradient(ellipse 140px 30px at 140px 110px,rgba(215,210,190,.85),transparent 70%),linear-gradient(180deg,#8fa1ad,#b4c1c8 40%,#4b6378)"></div><h4>Sed ut perspiciatisun de omnis iste nloreatrsit volu lore ptatnloreatrsit volu lore ptatem</h4><span class="arrow"><svg width="8" height="10" viewBox="0 0 8 10"><path d="M2 1l4 4-4 4" stroke="#fff" stroke-width="1.6" fill="none"/></svg></span></div>
      <div class="card"><div class="photo" role="img" aria-label="Two anglers casting from the boat deck" style="background:radial-gradient(ellipse 80px 110px at 90px 130px,rgba(150,160,110,.8),transparent 70%),radial-gradient(ellipse 80px 110px at 190px 130px,rgba(235,235,232,.9),transparent 70%),linear-gradient(180deg,#a7bdd0,#c9d4da 50%,#6e7d74)"></div><h4>Sed ut perspiciatisun de omnis iste nloreatrsit volu lore ptatnloreatrsit volu lore ptatem</h4><span class="arrow"><svg width="8" height="10" viewBox="0 0 8 10"><path d="M2 1l4 4-4 4" stroke="#fff" stroke-width="1.6" fill="none"/></svg></span></div>
      <div class="card"><div class="photo" role="img" aria-label="Young angler holding up a snook" style="background:radial-gradient(ellipse 90px 110px at 130px 120px,rgba(245,245,245,.9),transparent 70%),radial-gradient(ellipse 130px 30px at 150px 120px,rgba(200,195,170,.8),transparent 70%),linear-gradient(180deg,#2a4f32,#5f7f5c 50%,#9eaa9a)"></div><h4>Sed ut perspiciatisun de omnis iste nloreatrsit volu lore ptatnloreatrsit volu lore ptatem</h4><span class="arrow"><svg width="8" height="10" viewBox="0 0 8 10"><path d="M2 1l4 4-4 4" stroke="#fff" stroke-width="1.6" fill="none"/></svg></span></div>
    </div>
  </div>
</section>

<section class="newsletter" role="img" aria-label="Dark background of an angler with rod at dusk">
  <h2>SUBSCRIBE NEWSLETTER</h2>
  <p class="tag">Go on the fishing trip of your lifetime.</p>
  <div class="signup"><span class="field">Email address</span><span class="submit">SUBSCRIBE</span></div>
</section>

<footer class="site-footer">
  <div class="footer-brand"><span class="brand-dot"></span>Capt. Wade Harlan</div>
  <p class="footer-about">Sed ut perspiciatis unde omnis iste natus error sit voluptatem accusantium dolore mque laudantium, totam rem ape.</p>
  <div class="payments" aria-label="Accepted payment methods"><span></span><span></span><span></span><span></span><span></span></div>

  <div class="footer-col col-services">
    <h4>SERVICES</h4>
    <ul><li>Alandit sed nulla</li><li>In ullamcorper</li><li>Est eget tempor</li><li>Cursus neque</li><li>Consectetuer</li><li>Honsectetuer</li></ul>
  </div>
  <div class="footer-col col-contact">
    <h4>CONTACT US</h4>
    <ul>
      <li><svg width="8" height="11" viewBox="0 0 8 11"><path d="M4 0a4 4 0 0 0-4 4c0 3 4 7 4 7s4-4 4-7a4 4 0 0 0-4-4z" fill="#fff"/><circle cx="4" cy="4" r="1.5" fill="#0b55a2"/></svg>Harborline Marina - Bayview</li>
      <li class="sub">Pelican Cove - Sandport</li>
      <li class="sub">Causeway Boat Ramp</li>
      <li class="sub">Marlin Street Boat Ramp</li>
      <li><svg width="9" height="9" viewBox="0 0 10 10"><path d="M2 0l2 2.5-1.2 1.3a6 6 0 0 0 3.4 3.4L7.5 6 10 8l-1.5 2C4 10 0 6 0 1.5z" fill="#fff"/></svg>TEL: 555-014-2290</li>
      <li><svg width="10" height="8" viewBox="0 0 10 8"><rect width="10" height="8" fill="#fff"/><path d="M0 0l5 4 5-4" stroke="#0b55a2" fill="none"/></svg>E-MAIL: captwade@mailbox.example</li>
    </ul>
  </div>
  <div class="footer-col col-badges">
    <h4>LOGOS</h4>
    <div class="badges"><span class="badge"></span><span class="badge b2"></span></div>
  </div>

  <div class="footer-bar">
    <span>© 2016 Harlan. All Copyrights are reserved &nbsp;Term of Use. Privacy Policy</span>
    <div class="social" aria-label="Social media links"><span></span><span></span><span></span><span></span><span></span></div>
  </div>
</footer>

</body>
</html>
```